Business Card Design for Loft Pictures

Hi we need a business card designed for a new aerial photography business we have started, we use UAV Drones to take photos for corporate, events, real estate, local government etc , the business name is Loft Pictures Australia, we have a facebook page that might help you come up with some designs - https://www.facebook.com/loftpicturesaustralia

We need to have and editable AI file so that we can use different names and contact details. details for one of the cards as follow:

Ned Harrow
phone: 03 5521 4736
Mobile: 0431 957 284
email: ned@loftpicturez.example
web: www.loftpictures.example

have now changed: Designer Payment:Committed

Target Market(s)

We are a Aerial Photography business using Drones and UAV

Industry/Entity Type

Business

Logo Text

Loft Pictures Australia

Requirements
Must have
• Colors to match logo and be part of Loft Pictures Brand

```html
<!DOCTYPE html>
<html lang="en">
<head>
<meta charset="utf-8">
<title>Loft Pictures Australia – Business Card</title>
<link rel="stylesheet" href="https://fonts.googleapis.com/css2?family=Orbitron:wght@500;700&display=swap">
<style>
  :root {
    --page: #ffffff;
    --card-dark: #2c3036;
    --card-mid: #3b4148;
    --card-light: #5a6570;
    --strip: #25282d;
    --bar: #1b1d21;
    --edge: #8a9098;
    --wordmark: #c3c6ca;
    --text-light: #d4d7da;
    --accent: #2aa9e2;
    --streak: #3f8fc4;
  }
  html, body {
    margin: 0;
    width: 1200px;
    height: 857px;
    overflow: hidden;
    background: var(--page);
    font-family: "Orbitron", "Arial", sans-serif;
  }
  .sheet { position: relative; width: 1200px; height: 857px; }
  .card {
    position: absolute;
    top: 28px;
    width: 556px;
    height: 800px;
    border-radius: 22px;
    overflow: hidden;
  }
  .card--back {
    left: 22px;
    background:
      radial-gradient(ellipse 90% 60% at 80% 100%, var(--card-light), transparent 70%),
      linear-gradient(180deg, var(--card-dark) 0%, var(--card-mid) 60%, #4a535c 100%);
  }
  .card--front {
    left: 622px;
    background:
      radial-gradient(ellipse 60% 40% at 45% 55%, #414a53, transparent 70%),
      linear-gradient(180deg, #353a41 0%, #2e3238 100%);
  }
  .light-streak {
    position: absolute;
    left: 0; top: 0;
    width: 240px; height: 800px;
    background: linear-gradient(100deg, rgba(63,143,196,0.35) 0%, rgba(63,143,196,0.18) 45%, rgba(63,143,196,0) 100%);
  }
  .side-strip {
    position: absolute;
    left: 450px; top: 0;
    width: 106px; height: 800px;
    background: var(--strip);
    border-left: 1.5px solid var(--edge);
  }
  .bar { position: absolute; background: var(--bar); }
  .bar--top { left: 0; top: 24px; width: 260px; height: 42px; }
  .bar--side { left: 450px; top: 540px; width: 36px; height: 260px; }
  .wordmark {
    position: absolute;
    left: 0; right: 0;
    text-align: center;
    color: var(--wordmark);
    font-weight: 700;
    line-height: 1;
    text-transform: uppercase;
  }
  .wordmark__main { display: block; font-size: 66px; letter-spacing: 2px; }
  .wordmark__sub { display: block; font-size: 40px; margin-top: 8px; }
  .wordmark__region { display: block; font-size: 20px; letter-spacing: 14px; margin-top: 14px; padding-left: 14px; }
  .card--back .wordmark { top: 262px; }
  .card--front .wordmark { top: 106px; left: 0; width: 520px; right: auto; }
  .web {
    position: absolute;
    top: 450px; left: 0; right: 0;
    margin: 0;
    text-align: center;
    font-size: 14px;
    font-weight: 500;
    letter-spacing: 1.5px;
    color: var(--text-light);
    white-space: nowrap;
  }
  .holder {
    position: absolute;
    top: 350px; left: 0; width: 520px;
    margin: 0;
    text-align: center;
    font-size: 30px;
    font-weight: 700;
    letter-spacing: 2px;
    color: var(--accent);
    white-space: nowrap;
  }
  .contact {
    position: absolute;
    right: 110px;
    top: 428px;
    margin: 0;
    text-align: right;
    color: var(--text-light);
    font-weight: 500;
    white-space: nowrap;
  }
  .contact__line { display: block; font-size: 24px; letter-spacing: 1.5px; line-height: 36px; }
  .contact__line--email { font-size: 15px; letter-spacing: 1px; line-height: 30px; margin-top: 6px; }
</style>
</head>
<body>
<main class="sheet">
  <section class="card card--back" aria-label="Card back">
    <div class="wordmark">
      <span class="wordmark__main">Loft</span>
      <span class="wordmark__sub">Pictures</span>
      <span class="wordmark__region">Australia</span>
    </div>
    <p class="web">WEB: WWW.LOFTPICTURES.EXAMPLE</p>
  </section>

  <section class="card card--front" aria-label="Card front">
    <div class="light-streak" role="img" aria-label="Blue light streak artwork"></div>
    <div class="side-strip"></div>
    <div class="bar bar--top"></div>
    <div class="bar bar--side"></div>
    <div class="wordmark">
      <span class="wordmark__main">Loft</span>
      <span class="wordmark__sub">Pictures</span>
      <span class="wordmark__region">Australia</span>
    </div>
    <p class="holder">NED HARROW</p>
    <p class="contact">
      <span class="contact__line">PHONE: 03 5521 4736</span>
      <span class="contact__line">MOBILE: 0431 957 284</span>
      <span class="contact__line contact__line--email">EMAIL: NED@LOFTPICTUREZ.EXAMPLE</span>
    </p>
  </section>
</main>
</body>
</html>
```